Website Wordpress Responsive Design and Development - Landscape Company

Site is currently under construction, but the old site needs a refresh.
Need a fully responsive wordpress website (built in Elementor or comparable theme).
Here's the way it looked prior :
https://oldpages.example/snap/20220330041341/http://tobbsmaplegrove.example/
Their current designer came up with a website sample and it looks terrible :
https://danwelkerimages.sitebuild.example/mysite/projects
Websites the client likes for some inspiration, but needs better than these :
https://www.corwentlandscapearchitects.example/
http://qvateliernj.example/
https://brackenpartners.example/
https://www.tallanbysinc.example/

Navigation includes :
• Home
• Complete structure of website content is available in the home page, yielding main information on services.
• Visually appealing but simple to use and navigate. Subtle amount of content, but enough for search engines to be able to read up the target phrases.
• Sections on the home page include :
▪ About - Information about the company and main service focus
▪ Gallery - Imagery categorized to include lightbox style zoom.
▪ Contact - Contact details and connection information
• About
• Bannered header
• Content appropriately formatted to subject
• Gallery
• Bannered header
• Each of the albums would have their own categorized image content
• Contact
• Bannered header
• Social Media connector available on all pages (like box, feed, etc) if applicable
• Content can be updated on all pages
• Basic Optimization for SEO with title tags, meta data where applicable.
• Vantora Metrics and Sitemap installed. (vantora account will be provided)
• Vantora Firm Directory and Crawl Desk Accounts created

```html
<!DOCTYPE html>
<html lang="en">
<head>
<meta charset="utf-8">
<title>Tobb's Maple Grove – Landscaping</title>
<link rel="stylesheet" href="https://fonts.googleapis.com/css2?family=Poppins:wght@400;500;600;700&family=Lato:wght@400;700&display=swap">
<style>
:root{
  --green:#1d8a2f;
  --green-dark:#16702a;
  --brown:#5b2c0e;
  --brown-dark:#4a230a;
  --mint:#f3fbf4;
  --ink:#222;
  --text:#444;
  --line:#d9e4da;
  --white:#fff;
  --star:#f2b01e;
}
*{box-sizing:border-box;margin:0;padding:0}
html,body{width:1200px;height:4501px;overflow:hidden}
body{position:relative;background:var(--mint);font-family:'Lato',sans-serif;color:var(--text)}
.abs{position:absolute}
h2.section-title{position:absolute;left:0;width:1200px;text-align:center;font-family:'Poppins',sans-serif;font-weight:500;font-size:32px;color:var(--ink);letter-spacing:1px}
.section-sub{position:absolute;left:0;width:1200px;text-align:center;font-size:13px;color:var(--text)}
.btn{position:absolute;display:flex;align-items:center;justify-content:center;background:var(--green);color:var(--white);font-family:'Poppins',sans-serif;font-size:12px;border-radius:20px;text-decoration:none}
.ph{position:absolute}

/* header */
.site-header{position:absolute;left:0;top:0;width:1200px;height:133px;background:var(--white)}
.brand{position:absolute;left:73px;top:28px;font-family:'Poppins',sans-serif;font-weight:700;font-size:34px;line-height:34px;color:var(--brown);letter-spacing:1px}
.brand-sub{position:absolute;left:76px;top:76px;font-family:'Poppins',sans-serif;font-weight:700;font-size:14px;color:var(--brown);letter-spacing:4px}
.top-contact{position:absolute;top:28px;display:flex;align-items:center;gap:9px;font-size:11px;line-height:13px;color:var(--ink)}
.top-contact .ico{width:28px;height:28px;border-radius:50%;background:var(--green);display:flex;align-items:center;justify-content:center}
.quote-btn{position:absolute;left:987px;top:28px;width:140px;height:32px;border-radius:16px;background:var(--brown);color:var(--white);font-family:'Poppins',sans-serif;font-size:12px;display:flex;align-items:center;justify-content:center;gap:10px}
.quote-btn .dot{width:16px;height:16px;border-radius:50%;background:var(--green);display:flex;align-items:center;justify-content:center}
.nav-rule{position:absolute;left:500px;top:76px;width:630px;height:1px;background:#eee}
.main-nav{position:absolute;top:89px;left:512px;display:flex;gap:46px;font-family:'Poppins',sans-serif;font-size:13px;color:var(--ink)}
.main-nav .active{color:var(--green);position:relative}
.main-nav .active:after{content:"";position:absolute;left:0;right:0;top:24px;height:2px;background:var(--green)}

/* hero */
.hero{position:absolute;left:0;top:133px;width:1200px;height:710px;background:linear-gradient(180deg,#6d8a5f 0%,#a79070 35%,#8c7a5a 55%,#5f8a3c 75%,#8aa06a 100%)}
.hero-title{position:absolute;left:0;top:440px;width:1200px;text-align:center;font-family:'Poppins',sans-serif;font-size:35px;line-height:41px;color:var(--white);letter-spacing:3px;font-weight:400}
.hero-title b{font-weight:600}
.hero-dots{position:absolute;left:1150px;top:436px;width:14px}
.hero-dots span{display:block;width:5px;height:5px;background:var(--white);border-radius:50%;margin:0 auto 11px}
.hero-dots .cur{width:22px;height:22px;margin-left:-4px;background:var(--green);color:var(--white);font-size:9px;line-height:22px;text-align:center;font-family:'Poppins',sans-serif}

/* about */
.about-photo{left:131px;top:961px;width:454px;height:419px;background:linear-gradient(135deg,#cfd9c7,#7fa86a 50%,#2f7d3b);clip-path:polygon(3% 4%,97% 2%,99% 96%,2% 98%)}
.badge{position:absolute;left:489px;top:1000px;width:96px;height:96px;border-radius:14px;background:var(--green);color:var(--white);text-align:center;font-family:'Poppins',sans-serif;padding-top:18px}
.badge b{font-size:30px;line-height:30px}
.badge small{display:block;font-size:10px;font-weight:600;margin-top:4px}
.about-text{position:absolute;left:629px;width:463px;font-size:12px;line-height:22px;color:var(--text)}
.about-h{position:absolute;left:629px;top:1136px;font-family:'Poppins',sans-serif;font-size:17px;color:var(--ink)}

/* services */
.card{position:absolute;top:1534px;width:332px;height:428px;background:var(--white);border:1px solid #e2e9e2}
.card.raised{box-shadow:0 4px 14px rgba(0,0,0,.12)}
.card .media{position:absolute;left:9px;top:9px;width:312px;height:204px}
.card .icon{position:absolute;left:146px;top:192px;width:40px;height:40px;border-radius:50%;background:var(--white);display:flex;align-items:center;justify-content:center}
.card h3{position:absolute;top:232px;left:0;width:100%;text-align:center;font-family:'Poppins',sans-serif;font-weight:500;font-size:21px;color:var(--ink);letter-spacing:1px}
.card .dots{position:absolute;top:264px;left:0;width:100%;text-align:center;font-size:10px;letter-spacing:2px;color:#999;line-height:6px}
.card p{position:absolute;top:280px;left:20px;width:292px;text-align:center;font-size:12.5px;line-height:22px;color:var(--text)}
.card .btn{left:95px;top:364px;width:140px;height:36px}

/* gallery */
.filters{position:absolute;left:0;top:2098px;width:1200px;display:flex;justify-content:center;gap:20px;font-family:'Poppins',sans-serif;font-size:12px;font-weight:500;color:var(--ink)}
.filters .on{color:var(--green)}
.tile.focus{outline:3px solid var(--green);outline-offset:-3px}

/* testimonials */
.avatar{position:absolute;top:2913px;width:102px;height:102px;border-radius:50%;background:linear-gradient(160deg,#e7e2dc,#b9a898)}
.quote-mark{position:absolute;top:2913px;width:24px;height:24px;border-radius:50%;background:var(--green);color:var(--white);font-family:'Poppins',sans-serif;font-size:16px;line-height:30px;text-align:center;font-weight:700}
.t-name{position:absolute;top:3032px;width:320px;text-align:center;font-family:'Poppins',sans-serif;font-weight:500;font-size:15px;color:var(--ink)}
.t-dots{position:absolute;top:3056px;width:320px;text-align:center;font-size:10px;color:#999;letter-spacing:2px;line-height:6px}
.t-text{position:absolute;top:3070px;width:320px;text-align:center;font-size:13px;line-height:22px;color:var(--text)}
.stars{position:absolute;top:3136px;width:320px;text-align:center;color:var(--star);font-size:9px;letter-spacing:1px}

/* cta */
.cta{left:114px;top:3287px;width:972px;height:189px;background:linear-gradient(135deg,#2f8f2c,#4aa638 50%,#2d8a2a)}
.cta-text{position:absolute;left:248px;top:3348px;font-family:'Poppins',sans-serif;font-weight:600;font-size:32px;line-height:37px;color:var(--white);letter-spacing:2px}
.cta-btn{left:728px;top:3362px;width:191px;height:49px;border-radius:25px;background:var(--brown);font-size:14px}

/* contact form */
.field{position:absolute;height:44px;background:var(--white);border:1px solid #dcdcdc;font-size:12px;color:var(--text);padding:0 10px;display:flex;align-items:center;justify-content:space-between}
.field.area{align-items:flex-start;padding-top:14px}

/* footer */
.footer{position:absolute;left:0;top:4060px;width:1200px;height:360px;background:var(--brown)}
.foot-brand{position:absolute;left:73px;top:4226px;font-family:'Poppins',sans-serif;font-weight:700;font-size:52px;line-height:52px;color:var(--white);letter-spacing:1px}
.foot-brand-sub{position:absolute;left:76px;top:4290px;font-family:'Poppins',sans-serif;font-weight:700;font-size:18px;color:var(--white);letter-spacing:5px}
.foot-h{position:absolute;top:4152px;font-family:'Poppins',sans-serif;font-size:17px;color:var(--white)}
.foot-h:after{content:"";position:absolute;left:0;top:30px;width:90px;height:2px;background:var(--green)}
.foot-links{position:absolute;left:383px;top:4206px;list-style:none;font-size:12.5px;line-height:22.7px;color:var(--white)}
.foot-links li:before{content:">";margin-right:10px}
.foot-contact{position:absolute;left:601px;color:var(--white);font-size:13px;line-height:16px;display:flex;gap:8px}
.foot-contact svg{flex:none;margin-top:2px}
.map{left:896px;top:4210px;width:229px;height:131px;background:linear-gradient(135deg,#e8ece6,#d6dfd3)}
.copy{position:absolute;left:73px;top:4455px;font-size:12px;color:var(--text)}
.copy b{color:var(--green);font-weight:700}
.social{position:absolute;top:4445px;width:36px;height:36px;border-radius:50%;background:var(--brown)}
.social.g{background:var(--green)}
</style>
</head>
<body>

<!-- Header -->
<header class="site-header">
  <div class="brand">TOBB'S</div>
  <div class="brand-sub">MAPLE GROVE</div>
  <div class="top-contact" style="left:616px">
    <span class="ico"><svg width="14" height="14" viewBox="0 0 24 24"><path fill="#fff" d="M6.6 10.8a15 15 0 0 0 6.6 6.6l2.2-2.2a1 1 0 0 1 1-.25 11.4 11.4 0 0 0 3.6.57 1 1 0 0 1 1 1V20a1 1 0 0 1-1 1A17 17 0 0 1 3 4a1 1 0 0 1 1-1h3.5a1 1 0 0 1 1 1c0 1.25.2 2.45.57 3.57a1 1 0 0 1-.25 1z"/></svg></span>
    <span>Call Us<br>(555) 010-2884</span>
  </div>
  <div class="top-contact" style="left:775px">
    <span class="ico"><svg width="14" height="14" viewBox="0 0 24 24"><path fill="#fff" d="M3 5h18v14H3z"/><path d="M3 5l9 7 9-7" stroke="#1d8a2f" stroke-width="2" fill="none"/></svg></span>
    <span>Email us<br>Tobb@TobbsMapleGrove.example</span>
  </div>
  <div class="quote-btn">Get A Quote <span class="dot"><svg width="8" height="8" viewBox="0 0 8 8"><path d="M2 1l3 3-3 3" stroke="#fff" stroke-width="1.5" fill="none"/></svg></span></div>
  <div class="nav-rule"></div>
  <nav class="main-nav">
    <span class="active">Home</span><span>About us</span><span>Our Services ▾</span><span>Gallery</span><span>Team</span><span>Contact us</span>
    <svg width="14" height="14" viewBox="0 0 24 24" style="margin-left:-10px;margin-top:2px"><circle cx="10" cy="10" r="7" stroke="#222" stroke-width="2.5" fill="none"/><path d="M15 15l6 6" stroke="#222" stroke-width="2.5"/></svg>
  </nav>
</header>

<!-- Hero -->
<section class="hero" role="img" aria-label="Stone house with gabled roof, surrounded by trees and a green lawn with a curving driveway at sunset"></section>
<h1 class="hero-title">Architecturally<br>Designed <b>Landscaping</b></h1>
<div class="hero-dots"><span></span><span class="cur">02</span><span></span><span></span></div>
<svg class="abs" style="left:0;top:700px" width="1200" height="145" viewBox="0 0 1200 145">
  <path d="M0 145V60C80 150 300 145 520 105C760 60 960 20 1200 40V145Z" fill="var(--mint)"/>
  <path d="M0 60C60 120 200 140 360 125C260 140 120 135 0 95Z" fill="var(--brown)"/>
  <path d="M520 128C760 60 980 25 1200 40V90C1000 50 780 75 520 128Z" fill="var(--green)"/>
</svg>

<!-- About -->
<h2 class="section-title" style="top:908px">About us</h2>
<div class="ph about-photo" role="img" aria-label="Gardener in a green apron watering potted flowers in a greenhouse"></div>
<div class="badge"><b>20</b><small>YEAR EXPERIENCE</small></div>
<p class="about-text" style="top:994px">At an early age, Tobb Harlan began mowing lawns for local families. As he got older, the number of lawn accounts began to grow. In 1998, Tobb Harlan incorporated his small maintenance company taking it to the next level. Today, Tobb's Maple Grove services over 200 residential, municipal, and commercial properties and works with several local builders.</p>
<div class="about-h">Who We Are</div>
<p class="about-text" style="top:1177px">Tobb's Maple Grove is a full service landscape construction and maintenance company. We have been servicing the community for over 20 years and in that time have established ourselves as a premier contractor in the Hamptons. We pride ourselves on quality work and excellent customer service.</p>
<div class="btn" style="left:629px;top:1308px;width:155px;height:40px">Read More</div>

<!-- Services -->
<h2 class="section-title" style="top:1440px">Service</h2>
<p class="section-sub" style="top:1492px">Lorem Ipsum is simply dummy text of the printing.</p>

<article class="card" style="left:63px">
  <div class="media" role="img" aria-label="Formal garden with colourful flower beds and a central fountain" style="background:linear-gradient(180deg,#6f9a4e,#8fae5a 55%,#c99aa0)"></div>
  <div class="icon"><svg width="22" height="22" viewBox="0 0 24 24" fill="none" stroke="var(--brown)" stroke-width="1.5"><path d="M4 20c4-2 12-2 16 0M12 18V8M12 8c-3 0-5-2-5-5 3 0 5 2 5 5zM12 10c3 0 5-2 5-5-3 0-5 2-5 5z"/></svg></div>
  <h3>Landscaping</h3><div class="dots">........</div>
  <p>Lorem Ipsum is simply dummy text of the printing and typesetting industry has been dummy text ever since the 1500</p>
  <div class="btn">View More</div>
</article>
<article class="card raised" style="left:433px">
  <div class="media" role="img" aria-label="Red ride-on lawn mower cutting a striped lawn" style="background:linear-gradient(180deg,#3e6b2a,#6aa03a 45%,#4f8a2c)"></div>
  <div class="icon"><svg width="22" height="22" viewBox="0 0 24 24" fill="none" stroke="var(--brown)" stroke-width="1.5"><circle cx="7" cy="17" r="3"/><circle cx="18" cy="18" r="2"/><path d="M7 14l3-7h4l4 9M3 5l4 2"/></svg></div>
  <h3>Maintenance</h3><div class="dots">........</div>
  <p>Lorem Ipsum is simply dummy text of the printing and typesetting industry has been dummy text ever since the 1500</p>
  <div class="btn">View More</div>
</article>
<article class="card" style="left:798px">
  <div class="media" role="img" aria-label="Pink roses climbing over a dark green fence" style="background:linear-gradient(135deg,#2f4a2a,#4f6e3a 50%,#c7677a)"></div>
  <div class="icon"><svg width="22" height="22" viewBox="0 0 24 24" fill="none" stroke="var(--brown)" stroke-width="1.5"><circle cx="12" cy="12" r="2.5"/><path d="M12 9.5c-2-5 2-5 0 0M14.4 11.2c4-3 5 1 0 0M13.5 14c3 4-1 5 0 0M10.5 14c-3 4-5 0 0 0M9.6 11.2c-4-3-5 1 0 0"/></svg></div>
  <h3>Flowers</h3><div class="dots">........</div>
  <p>Lorem Ipsum is simply dummy text of the printing and typesetting industry has been dummy text ever since the 1500</p>
  <div class="btn">View More</div>
</article>

<!-- Gallery -->
<h2 class="section-title" style="top:2044px">Gallery</h2>
<div class="filters"><span class="on">All</span><span>Gardens</span><span>Interiors</span><span>Maintance</span><span>Flower</span></div>
<div class="ph tile" role="img" aria-label="Half-timbered cottage behind a garden full of red and pink flowers" style="left:73px;top:2136px;width:330px;height:547px;background:linear-gradient(180deg,#7db0d8,#e6e2d6 40%,#4f8a3a 70%,#b8424a)"></div>
<div class="ph tile" role="img" aria-label="Modern timber house lit warmly at dusk" style="left:430px;top:2136px;width:328px;height:259px;background:linear-gradient(180deg,#1f2d45,#4a3a30 60%,#c08a4a)"></div>
<div class="ph tile" role="img" aria-label="Grey craftsman house with shrubs and a front lawn" style="left:782px;top:2136px;width:341px;height:259px;background:linear-gradient(180deg,#c9dcea,#6f7884 55%,#5c8c3c)"></div>
<div class="ph tile focus" role="img" aria-label="Large house with a landscaped front garden, darkened for zoom preview" style="left:430px;top:2424px;width:442px;height:259px;background:linear-gradient(180deg,#2f3436,#3f4640 60%,#2f3f2a)"></div>
<svg class="abs" style="left:628px;top:2540px" width="26" height="26" viewBox="0 0 26 26" fill="none" stroke="#fff" stroke-width="1.6"><rect x="2" y="2" width="22" height="22" rx="2"/><path d="M8 13h10M13 8v10M6 6l4 4M20 20l-4-4"/></svg>
<div class="ph tile" role="img" aria-label="White colonial house with a dark front door and manicured lawn" style="left:898px;top:2424px;width:227px;height:259px;background:linear-gradient(180deg,#dfe6ea,#b8bec4 50%,#4c8a34)"></div>
<div class="btn" style="left:533px;top:2720px;width:138px;height:35px">View More</div>

<!-- Testimonials -->
<h2 class="section-title" style="top:2815px">Testimonials</h2>
<p class="section-sub" style="top:2864px">What Clients Say About us</p>

<div class="avatar" style="left:190px" role="img" aria-label="Client portrait"></div><div class="quote-mark" style="left:190px">"</div>
<div class="t-name" style="left:81px">Nora Jameson</div><div class="t-dots" style="left:81px">......</div>
<p class="t-text" style="left:81px">Lorem Ipsum is simply dummy text of the printing and typesetting industry has been dummy text ever since the 1500</p>
<div class="stars" style="left:81px">★★★★★</div>

<div class="avatar" style="left:550px" role="img" aria-label="Client portrait"></div><div class="quote-mark" style="left:550px">"</div>
<div class="t-name" style="left:441px">Selma Jonas</div><div class="t-dots" style="left:441px">......</div>
<p class="t-text" style="left:441px">Lorem Ipsum is simply dummy text of the printing and typesetting industry has been dummy text ever since the 1500</p>
<div class="stars" style="left:441px">★★★★★</div>

<div class="avatar" style="left:904px" role="img" aria-label="Client portrait"></div><div class="quote-mark" style="left:904px">"</div>
<div class="t-name" style="left:795px">Kristof Aldane</div><div class="t-dots" style="left:795px">......</div>
<p class="t-text" style="left:795px">Lorem Ipsum is simply dummy text of the printing and typesetting industry has been dummy text ever since the 1500</p>
<div class="stars" style="left:795px">★★★★★</div>

<svg class="abs" style="left:572px;top:3190px" width="52" height="6"><circle cx="3" cy="3" r="2" fill="var(--ink)"/><rect x="10" y="1.5" width="20" height="3" rx="1.5" fill="var(--green)"/><circle cx="37" cy="3" r="2" fill="var(--ink)"/><circle cx="45" cy="3" r="2" fill="var(--ink)"/></svg>

<!-- CTA -->
<div class="ph cta" role="img" aria-label="Close-up of fresh green grass"></div>
<div class="cta-text">Get A Free Online Quote<br>In Under 24 Hours</div>
<div class="btn cta-btn">Get A Quote</div>

<!-- Quick Contact -->
<h2 class="section-title" style="top:3562px">Quick Contact</h2>
<div class="field" style="left:246px;top:3626px;width:228px">First Name*</div>
<div class="field" style="left:485px;top:3626px;width:228px">Last Name*</div>
<div class="field" style="left:724px;top:3626px;width:228px">Email*</div>
<div class="field" style="left:246px;top:3680px;width:228px">Phone*</div>
<div class="field" style="left:485px;top:3680px;width:228px">Type of Property<span>⌄</span></div>
<div class="field" style="left:724px;top:3680px;width:228px">Job Category<span>⌄</span></div>
<div class="field area" style="left:246px;top:3734px;width:706px;height:158px">Message</div>
<div class="btn" style="left:533px;top:3911px;width:138px;height:35px">Send</div>

<!-- Footer -->
<svg class="abs" style="left:0;top:3990px" width="1200" height="75" viewBox="0 0 1200 75">
  <path d="M0 35C250 95 550 20 800 20C950 20 1100 40 1200 45V75H0Z" fill="var(--brown)"/>
  <path d="M0 15C120 60 300 60 480 40C620 25 740 15 800 18C600 30 300 90 0 40Z" fill="var(--green)"/>
</svg>
<footer class="footer"></footer>
<div class="foot-brand">TOBB'S</div>
<div class="foot-brand-sub">MAPLE GROVE</div>

<div class="foot-h" style="left:383px">Quick Links</div>
<ul class="foot-links"><li>Home</li><li>About us</li><li>Our Services</li><li>Gallery</li><li>Team</li><li>Contact us</li></ul>

<div class="foot-h" style="left:601px">Contact Detail</div>
<div class="foot-contact" style="top:4210px"><svg width="12" height="12" viewBox="0 0 24 24"><path fill="var(--green)" d="M6.6 10.8a15 15 0 0 0 6.6 6.6l2.2-2.2a1 1 0 0 1 1-.25 11.4 11.4 0 0 0 3.6.57 1 1 0 0 1 1 1V20a1 1 0 0 1-1 1A17 17 0 0 1 3 4a1 1 0 0 1 1-1h3.5a1 1 0 0 1 1 1c0 1.25.2 2.45.57 3.57a1 1 0 0 1-.25 1z"/></svg><span>(555) 010-2884<br>(555) 010-9263</span></div>
<div class="foot-contact" style="top:4279px"><svg width="12" height="12" viewBox="0 0 24 24"><path fill="var(--green)" d="M3 5h18v14H3z"/></svg><span>Tobb@TobbsMapleGrove.example</span></div>
<div class="foot-contact" style="top:4318px"><svg width="12" height="12" viewBox="0 0 24 24"><path fill="var(--green)" d="M12 2a7 7 0 0 0-7 7c0 5 7 13 7 13s7-8 7-13a7 7 0 0 0-7-7zm0 9.5A2.5 2.5 0 1 1 12 6.5a2.5 2.5 0 0 1 0 5z"/></svg><span>PO Box 218<br>Alder Falls, NY 10999</span></div>

<div class="foot-h" style="left:893px">Map</div>
<div class="ph map" role="img" aria-label="Area map showing the office location"></div>

<p class="copy">Copyright © 2022 <b>TOBB'S MAPLE GROVE</b>. All Rights Reserved.</p>
<div class="social g" style="left:944px" aria-label="Social link 1"></div>
<div class="social" style="left:993px" aria-label="Social link 2"></div>
<div class="social" style="left:1042px" aria-label="Social link 3"></div>
<div class="social" style="left:1088px" aria-label="Social link 4"></div>

</body>
</html>
```